Harrowgate Estates Business Card for Apartment Buildings

Create business cards for resident managers who run apartment buildings. The audience is the public who are searching for apartment rentals, and current residents who live at the apartment building. Key design element will be incorporating the company logo, however, the logo cannot dominate. The building name and manager name are more important than the logo. Current business card design leaves little room for copy, so we may need to reduce the size on the current card to allow for more space for copy.

Target Market(s)

Adults 18-65 years of age, who are looking for an apartment rental, plus current residents who live at our apartment buildings.

Industry/Entity Type

Property Management

Contact Information for Business Card

A major design element will be use of the company logo. Important property and manager contact information must be part of the design. The size of the logo will need to be reduced to make room for building and manager contact copy.

Font styles to use
Sans Serif

Colors
3176b5
000000
959595
ffffff

Requirements
Must have
• 1) Incorporate the company logo.
• 2) Use the company colors (dark blue, black/grey, over white).
• 3) FEATURE THE BUILDING NAME
• 4) FEATURE THE MANAGER NAME
• 5) The company name is less important than BUILDING and MANAGER
• 6) Manager contact information
• **SEE ATTACHED CREATIVE BRIEF**
Nice to have
• 1) Back of card logo watermark
• 2) Ability to write notes on back of carfd
Should not have
• Avoid letting the company logo dominate the card, the building name and manager are more important than the company logo.

```html
<!DOCTYPE html>
<html lang="en">
<head>
<meta charset="utf-8">
<title>Harrowgate Estates – Business Card</title>
<link href="https://fonts.googleapis.com/css2?family=Roboto:wght@400;700&display=swap" rel="stylesheet">
<style>
  :root {
    --brand-blue: #0f63a6;
    --ink-grey: #4a4a4b;
    --text-grey: #444444;
    --mark-grey: #4a4a4b;
    --watermark: #e6e8ee;
    --card-white: #ffffff;
    --stage: #eeeeee;
  }
  * { margin: 0; padding: 0; box-sizing: border-box; }
  html, body {
    width: 1200px; height: 960px; overflow: hidden;
    background: var(--stage);
    font-family: "Roboto", Arial, sans-serif;
  }
  .canvas { position: relative; width: 1200px; height: 960px; }
  .card {
    position: absolute; left: 273px; width: 655px; height: 374px;
    background: var(--card-white);
    box-shadow: 0 2px 6px rgba(0,0,0,0.18);
  }
  .card--front { top: 80px; }
  .card--back { top: 506px; }

  .company-name {
    position: absolute; left: 39px; top: 32px;
    color: var(--brand-blue); font-weight: 700; font-size: 30px;
    line-height: 32px; letter-spacing: 0.5px;
  }
  .manager-name {
    position: absolute; left: 40px; top: 128px;
    color: var(--brand-blue); font-weight: 700; font-size: 20px;
  }
  .manager-title {
    position: absolute; left: 40px; top: 155px;
    color: var(--text-grey); font-size: 15px;
  }
  .building-name {
    position: absolute; left: 40px; top: 196px;
    color: var(--brand-blue); font-size: 14.5px;
  }
  .building-address {
    position: absolute; left: 40px; top: 218px;
    color: var(--text-grey); font-size: 14.5px;
  }
  .contact-list { position: absolute; left: 40px; top: 256px; list-style: none; }
  .contact-list li {
    display: flex; align-items: center; height: 22px;
    color: var(--text-grey); font-size: 14.5px;
  }
  .contact-list svg { width: 15px; height: 15px; margin-right: 9px; fill: var(--brand-blue); }

  .brand-circle { position: absolute; left: 369px; top: 65px; }
  .watermark { position: absolute; left: 0; top: 0; }
</style>
</head>
<body>
<main class="canvas">
  <section class="card card--front">
    <div class="company-name">HARROWGATE<br>ESTATES LLC</div>

    <div class="manager-name">Marisol Quintero</div>
    <div class="manager-title">Resident Manager</div>

    <div class="building-name">Linden Court Apartments</div>
    <div class="building-address">2458 Fairmount Avenue, Riverton, CA 94817</div>

    <ul class="contact-list">
      <li>
        <svg viewBox="0 0 16 16" aria-hidden="true"><path d="M4 1l3 3-2 2c1 2 3 4 5 5l2-2 3 3-2 2C7 15 1 9 2 3z"/></svg>
        555-201-4830
      </li>
      <li>
        <svg viewBox="0 0 16 16" aria-hidden="true"><path d="M1 5h14v3H1zM3 9h10v6H3zM5 11h6v1H5zM4 1h8v3H4z"/></svg>
        555-201-4831
      </li>
      <li>
        <svg viewBox="0 0 16 16" aria-hidden="true"><path d="M1 3h14v10H1zM2 4l6 5 6-5v1l-6 5-6-5z" fill-rule="evenodd"/></svg>
        555-201-4832
      </li>
      <li>
        <svg viewBox="0 0 16 16" aria-hidden="true"><path fill="none" stroke="currentColor" d="M8 1a7 7 0 1 0 0 14A7 7 0 1 0 8 1zM1 8h14M8 1c-3 3-3 11 0 14M8 1c3 3 3 11 0 14M2.5 4.5h11M2.5 11.5h11" style="stroke:var(--brand-blue)"/></svg>
        marisol@harrowgate.com
      </li>
    </ul>

    <svg class="brand-circle" width="244" height="244" viewBox="0 0 244 244" aria-hidden="true">
      <circle cx="122" cy="122" r="116" fill="none" stroke="var(--mark-grey)" stroke-width="7"/>
    </svg>
  </section>

  <section class="card card--back" aria-label="Card back with space for notes">
    <svg class="watermark" width="655" height="374" viewBox="0 0 655 374" aria-hidden="true">
      <circle cx="327" cy="187" r="118" fill="none" stroke="var(--watermark)" stroke-width="8"/>
      <text x="327" y="183" text-anchor="middle" font-family="Roboto, Arial, sans-serif" font-weight="700" font-size="26" fill="var(--watermark)">HARROWGATE</text>
      <text x="327" y="213" text-anchor="middle" font-family="Roboto, Arial, sans-serif" font-weight="700" font-size="26" fill="var(--watermark)">ESTATES LLC</text>
    </svg>
  </section>
</main>
</body>
</html>
```